Communications Contractor Business Card Design

I would like a new business card for a new Communications company in Australia. Subcontracting and specialising in cabling, data, phone, antennas, pay tv ,modems, audio visual fibre optics etc. I am open to colour and design concepts but would like a modern clean look that stands out.

Industry/Entity Type

Tv

Contact Information for Business Card

quarzel communications pty ltd, Tomas Whitlock, PO BOX 527 Morrendale Flats QLD 4390 quarzel4me@mailbrook.net Australia. ph 0438271906. Director/Technician. services- Cabling,data,phone,antennas,audio visual,home theatre, fibre optics.

```html
<!DOCTYPE html>
<html lang="en">
<head>
<meta charset="utf-8">
<title>Quarzel Communications – Business Card</title>
<link rel="stylesheet" href="https://fonts.googleapis.com/css2?family=Arimo:wght@400;700&family=PT+Sans:wght@400&display=swap">
<style>
  :root {
    --page-bg: #e4e4e4;
    --brand-blue: #1a82bf;
    --brand-blue-soft: #2a8ecb;
    --accent-blue: #3498d8;
    --wave-blue: #2b93d1;
    --ink: #1d1d1d;
    --ink-soft: #2a2a2a;
    --card-white: #ffffff;
    --divider: #6b6b6b;
  }
  * { box-sizing: border-box; margin: 0; padding: 0; }
  html, body {
    width: 1200px;
    height: 920px;
    overflow: hidden;
    background: var(--page-bg);
    font-family: "Arimo", Arial, sans-serif;
  }
  .canvas {
    position: relative;
    width: 1200px;
    height: 920px;
  }
  .card {
    position: absolute;
    width: 610px;
    height: 354px;
    overflow: hidden;
  }

  /* Back of card */
  .card-back {
    left: 108px;
    top: 88px;
    background: var(--brand-blue);
  }
  .card-back .cable-art {
    position: absolute;
    left: 0;
    top: 14px;
    width: 222px;
    height: 330px;
    background: linear-gradient(160deg, var(--brand-blue-soft), var(--brand-blue) 85%);
  }
  .card-back .services {
    position: absolute;
    right: 38px;
    top: 269px;
    color: var(--card-white);
    font-size: 16px;
    line-height: 21px;
    text-align: right;
  }
  .services span { display: block; }

  /* Front of card */
  .card-front {
    left: 501px;
    top: 487px;
    background: var(--card-white);
  }
  .company-name {
    position: absolute;
    left: 106px;
    top: 106px;
    font-family: "PT Sans", Arial, sans-serif;
    font-weight: 400;
    font-size: 28px;
    color: var(--brand-blue);
    white-space: nowrap;
  }
  .person {
    position: absolute;
    right: 334px;
    top: 207px;
    text-align: right;
  }
  .person-name {
    font-weight: 700;
    font-size: 26px;
    color: var(--accent-blue);
    line-height: 30px;
  }
  .person-role {
    font-size: 14px;
    color: var(--ink);
    margin-top: 2px;
  }
  .divider {
    position: absolute;
    left: 306px;
    top: 191px;
    width: 1px;
    height: 82px;
    background: var(--divider);
  }
  .contact {
    position: absolute;
    left: 332px;
    top: 189px;
    font-size: 14px;
    color: var(--ink-soft);
    line-height: 19px;
  }
  .contact-address { margin-bottom: 11px; }
  .contact-line {
    display: flex;
    align-items: center;
    gap: 7px;
  }
  .contact-line svg { flex: none; }
  .wave {
    position: absolute;
    left: 0;
    bottom: 0;
    width: 610px;
    height: 60px;
  }
</style>
</head>
<body>
<main class="canvas">

  <section class="card card-back" aria-label="Business card back">
    <div class="cable-art" role="img" aria-label="Faint cable and plug illustration"></div>
    <p class="services">
      <span>Data - Phone - Antennas</span>
      <span>Audio visual - Home theatre - Fibre optics</span>
    </p>
  </section>

  <section class="card card-front" aria-label="Business card front">
    <h1 class="company-name">Quarzel Communications Pty Ltd</h1>

    <div class="person">
      <p class="person-name">Tomas Whitlock</p>
      <p class="person-role">Director/Technician</p>
    </div>

    <div class="divider"></div>

    <div class="contact">
      <p class="contact-address">PO BOX 527<br>Morrendale Flats QLD 4390</p>
      <p class="contact-line">
        <svg width="12" height="12" viewBox="0 0 24 24" aria-hidden="true">
          <path fill="#3498d8" d="M6.6 10.8a15.1 15.1 0 0 0 6.6 6.6l2.2-2.2c.3-.3.7-.4 1-.2 1.1.4 2.3.6 3.6.6.6 0 1 .4 1 1V20c0 .6-.4 1-1 1C10.6 21 3 13.4 3 4c0-.6.4-1 1-1h3.5c.6 0 1 .4 1 1 0 1.3.2 2.5.6 3.6.1.3 0 .7-.2 1l-2.3 2.2z"/>
        </svg>
        043-827-1906
      </p>
      <p class="contact-line">
        <svg width="12" height="10" viewBox="0 0 24 18" aria-hidden="true">
          <path fill="#3498d8" d="M0 0h24v18H0z"/>
          <path fill="none" stroke="#fff" stroke-width="2" d="M1 1l11 9 11-9"/>
        </svg>
        quarzel4me@mailbrook.net
      </p>
    </div>

    <svg class="wave" viewBox="0 0 610 60" preserveAspectRatio="none" aria-hidden="true">
      <path fill="#1d1d1d" d="M0 4 C90 20 180 30 270 30 S480 20 610 32 L610 60 L0 60 Z"/>
      <path fill="#ffffff" d="M0 11 C90 27 180 34 270 34 S480 24 610 35 L610 60 L0 60 Z"/>
      <path fill="#2b93d1" d="M0 15 C90 30 180 37 270 37 S480 27 610 38 L610 60 L0 60 Z"/>
    </svg>
  </section>

</main>
</body>
</html>
```